Fretwise Riff Hall WebSite

I am looking for a website design for FretwiseRiffHall.com. If you are unfamiliar with the term "guitar lick": a guitar lick is a simple piece of music that is used in an improvisation or solo. All of the famous guitarists that you probably have heard of (Tobin Marlowe, Dale Pemberly, etc.) have their own set of unique licks. This is what defines their style. The "Dojo" in the site name refers to a karate dojo. Basically, like a person would master karate in a karate dojo, a guitarist can master guitar licks in the Fretwise Riff Hall. The purpose of FretwiseRiffHall is to show users very high quality videos (vidstreamo) and music notation for a variety of licks. Many of the guitar licks on the site will be from famous guitarists. There will also be licks that are not from famous guitarists, that are just general licks in a particular style or genre.

Target Market(s)

Intermediate and above guitar players.

Industry/Entity Type

Vidstreamo

Requirements
Must have
• 1) The look and feel of the site must be based on the logo that I have attached. First and foremost, this site must be FUN. The page should fit with the mood of the logo. The logo should be incorporated well into the header design. It would be nice to see the logo theme used throughout the same page in some creative and reasonable way.
• 2) There will be three main navigation tabs on the home page: Licks, JamTracks, and Blog. The Licks section will be broken into Licks by Artist, and licks by genre (eg. Jazz, Rock, Blues, Fusion, Heavy Metal, Country, etc.)
• 3) There needs to be 3 main sections on the Home Page: Lick of the Day, Recently Added Licks, and Featured Licks. These 3 sections must contain thumbnails of the videos, along with a text description.
Nice to have
• Use the character from the logo or the karate theme in some creative way on the page.

```html
<!DOCTYPE html>
<html lang="en">
<head>
<meta charset="utf-8">
<title>Fretwise Riff Hall</title>
<link href="https://fonts.googleapis.com/css2?family=Arvo:wght@400;700&family=Open+Sans:ital,wght@0,300;0,400;0,600;0,700;1,300;1,400&display=swap" rel="stylesheet">
<style>
:root{
  --red:#e0141e;
  --red-dark:#8c0a10;
  --heading-red:#c41a22;
  --black:#0b0b0b;
  --header:#1a1a1a;
  --page:#d8d8d8;
  --text:#5a5a5a;
  --muted:#8a8a8a;
  --white:#ffffff;
  --blue:#1aa3d8;
  --line:#b9b9b9;
}
*{box-sizing:border-box;margin:0;padding:0}
html,body{width:1200px;height:3061px;overflow:hidden}
body{position:relative;background:var(--page);font-family:"Open Sans",Arial,sans-serif;color:var(--text)}

/* top bar */
.topbar{position:absolute;left:0;top:0;width:1200px;height:41px;background:var(--black)}
.topbar .connect{position:absolute;right:206px;top:10px;color:#fff;font-size:14px;font-weight:600;white-space:nowrap}
.topbar .social{position:absolute;top:8px;width:24px;height:24px;border-radius:3px}

/* header */
.site-header{position:absolute;left:0;top:41px;width:1200px;height:153px;background:linear-gradient(#262626,#151515)}
.brand{position:absolute;left:110px;top:56px;display:flex;align-items:center;gap:12px}
.brand-mark{width:44px;height:44px;border-radius:50%;background:var(--red)}
.brand-name{font-family:"Arvo",Georgia,serif;font-weight:700;font-size:24px;color:#fff}
.search{position:absolute;left:743px;top:57px;width:347px;height:41px;display:flex}
.search-field{flex:1;background:#fff;border:1px solid #ccc;padding:0 14px;font-size:15px;font-style:italic;color:#999;line-height:39px}
.search-btn{width:43px;background:#b3141b;display:flex;align-items:center;justify-content:center}

.main-nav{position:absolute;left:0;top:194px;width:1200px;height:57px;background:linear-gradient(#3a0306,#a8121a 50%,#3a0306)}
.main-nav a{position:absolute;top:19px;font-family:"Arvo",Georgia,serif;font-weight:700;font-size:16px;color:#fff;text-decoration:none;letter-spacing:.5px}

/* hero */
.hero{position:absolute;left:0;top:251px;width:1200px;height:535px}
.hero-photo{position:absolute;inset:0;background:radial-gradient(ellipse at 75% 45%,#4a4a4a 0%,#242424 40%,#0c0c0c 75%),#111}
.hero-photo::after{content:"";position:absolute;left:0;right:0;bottom:0;height:80px;background:linear-gradient(transparent,rgba(160,10,18,.55))}
.hero-title{position:absolute;left:110px;top:118px;font-family:"Arvo",Georgia,serif;font-weight:700;font-size:66px;color:var(--red);line-height:1}
.hero-sub{position:absolute;left:250px;top:190px;font-size:22px;font-style:italic;font-weight:300;color:#fff}
.hero-list{position:absolute;left:112px;top:243px;list-style:none}
.hero-list li{display:flex;align-items:center;gap:22px;height:60px;font-size:20px;font-style:italic;font-weight:300;color:#fff}
.hero-list svg{width:26px;height:26px}

/* section headings */
.section-title{position:absolute;left:0;width:1200px;text-align:center;font-family:"Arvo",Georgia,serif;font-weight:700;font-size:28px;color:#2a2a2a}
.rule{position:absolute;left:60px;width:1080px;height:2px;background:linear-gradient(90deg,transparent,var(--line) 15%,var(--line) 85%,transparent)}

/* guitar decoration */
.guitar{position:absolute;border-radius:40px}

/* video cards */
.video-card{position:absolute;width:237px;height:372px;overflow:hidden}
.video-card .thumb{position:absolute;inset:0;background:radial-gradient(ellipse at 50% 35%,#4d4d4d,#1e1e1e 70%)}
.video-card .shade{position:absolute;inset:0;background:rgba(0,0,0,.45)}
.video-card.active .thumb{background:radial-gradient(ellipse at 50% 35%,#6fd0f2,#1aa3d8 70%)}
.video-card.active .shade{display:none}
.video-card .play{position:absolute;left:86px;top:128px;width:66px;height:66px}
.video-card .card-title{position:absolute;left:14px;top:268px;font-size:19px;font-weight:600;color:#fff}
.video-card .card-sub{position:absolute;left:14px;top:295px;font-size:12px;color:#bdbdbd}
.video-card.active .card-sub{color:#fff}
.share{position:absolute;left:18px;top:328px;display:flex;gap:22px;align-items:center}
.share i{display:block;width:16px;height:16px;border-radius:50%;background:#9a9a9a}
.share svg{width:20px;height:16px}
.video-card.active .share i{background:#fff}

/* side text blocks */
.side-block{position:absolute;left:110px;width:237px}
.side-block h2{font-family:"Arvo",Georgia,serif;font-weight:700;font-size:27px;line-height:35px;color:var(--heading-red)}
.side-block p{font-size:12.5px;line-height:20px;margin-top:14px;color:var(--text)}
.pager{display:flex;gap:6px;margin-top:18px}
.pager span{width:26px;height:26px;border-radius:50%;background:#555;display:flex;align-items:center;justify-content:center}

/* blog */
.post{position:absolute;width:500px}
.post .post-thumb{position:absolute;left:0;top:0;width:146px;height:106px}
.post .post-body{position:absolute;left:161px;top:0;width:330px}
.post h3{font-family:"Arvo",Georgia,serif;font-weight:700;font-size:15.5px;line-height:22px;color:var(--heading-red)}
.post p{font-size:12.5px;line-height:20px;margin-top:2px;color:var(--text)}
.post p + p{margin-top:14px}

/* footer */
.site-footer{position:absolute;left:0;top:2729px;width:1200px;height:281px;background:var(--black);color:#ddd}
.footer-col{position:absolute;top:20px}
.footer-col h4{font-size:14px;font-weight:600;color:#fff;display:flex;align-items:center;gap:8px;text-transform:uppercase;white-space:nowrap}
.footer-col h4 svg{width:14px;height:14px}
.quick-links{list-style:none;margin-top:20px;margin-left:16px}
.quick-links li{font-size:13px;line-height:20.5px;color:#ddd}
.footer-social{display:flex;gap:26px;margin-top:36px;margin-left:24px;align-items:center}
.footer-social i{display:block;width:18px;height:18px;border-radius:50%;background:#e0e0e0}
.comments{width:340px}
.comment{display:flex;gap:14px;margin-top:20px}
.comment + .comment{margin-top:14px}
.avatar{width:52px;height:52px;background:#c9c9c9;flex:none}
.comment-text{width:272px}
.comment small{display:block;font-size:10px;font-style:italic;color:var(--red);line-height:14px}
.comment p{font-size:11px;line-height:18px;font-style:italic;color:#ddd}
.newsletter{width:314px}
.newsletter p{font-size:12.5px;line-height:20px;margin-top:20px;width:314px}
.email-field{margin-top:18px;width:314px;height:42px;border:1px solid #444;background:#0b0b0b;font-size:13px;color:#ddd;padding:0 14px;line-height:40px}
.submit-btn{margin-top:9px;margin-left:173px;width:141px;height:41px;background:var(--red);color:#fff;font-weight:700;font-size:15px;text-align:center;line-height:41px;border-radius:2px;text-transform:uppercase}

.bottom-bar{position:absolute;left:0;top:3010px;width:1200px;height:51px;background:#d4d4d4;font-size:12px;color:#444}
.bottom-bar .copy{position:absolute;left:110px;top:17px}
.bottom-bar .legal{position:absolute;right:110px;top:17px}
</style>
</head>
<body>

<div class="topbar">
  <span class="connect">Connect With Us:</span>
  <span class="social" style="left:1008px;background:#3b5998"></span>
  <span class="social" style="left:1037px;background:#3fa9e0"></span>
  <span class="social" style="left:1066px;background:#c4302b"></span>
</div>

<header class="site-header">
  <div class="brand">
    <span class="brand-mark"></span>
    <span class="brand-name">Fretwise Riff Hall</span>
  </div>
  <div class="search">
    <div class="search-field">Search..</div>
    <div class="search-btn">
      <svg width="20" height="20" viewBox="0 0 20 20"><circle cx="8" cy="8" r="6" fill="none" stroke="#fff" stroke-width="2"/><line x1="12.5" y1="12.5" x2="18" y2="18" stroke="#fff" stroke-width="2.4"/></svg>
    </div>
  </div>
</header>

<nav class="main-nav">
  <a style="left:701px">HOME</a>
  <a style="left:800px">LICKS</a>
  <a style="left:895px">JAMTRACKS</a>
  <a style="left:1042px">BLOG</a>
</nav>

<section class="hero">
  <div class="hero-photo" role="img" aria-label="Photo of a guitarist playing an electric guitar in dim stage light"></div>
  <h1 class="hero-title">Jam Tracks</h1>
  <p class="hero-sub">High Quality Backing Tracks</p>
  <ul class="hero-list">
    <li><svg viewBox="0 0 26 26"><path d="M9 20V6l12-3v14" fill="none" stroke="#e0141e" stroke-width="2.2"/><circle cx="6.5" cy="20" r="3.5" fill="#e0141e"/><circle cx="18.5" cy="17" r="3.5" fill="#e0141e"/></svg>Many styles to choose from</li>
    <li><svg viewBox="0 0 26 26"><circle cx="13" cy="13" r="11" fill="none" stroke="#e0141e" stroke-width="2.4"/><circle cx="13" cy="13" r="3.5" fill="#e0141e"/></svg>High quality mp3 format</li>
    <li><svg viewBox="0 0 26 26"><path d="M13 2v14M7 10l6 6 6-6" fill="none" stroke="#e0141e" stroke-width="3"/><rect x="3" y="20" width="20" height="4" fill="#e0141e"/></svg>Istant Download</li>
  </ul>
</section>

<!-- Lick of the day -->
<h2 class="section-title" style="top:806px">LICK OF THE DAY</h2>
<div class="rule" style="top:866px"></div>
<div class="guitar" role="img" aria-label="Illustration of an electric guitar with sunburst body" style="left:24px;top:832px;width:88px;height:440px;background:linear-gradient(#d8d8d8 0%,#bfbfbf 10%,#6b3a1a 55%,#3a1608 80%,#c7c7c7 100%)"></div>

<div class="video-card" style="left:110px;top:900px">
  <div class="thumb" role="img" aria-label="Video still of a guitarist playing"></div><div class="shade"></div>
  <svg class="play" viewBox="0 0 66 66"><circle cx="33" cy="33" r="32" fill="rgba(255,255,255,.25)"/><path d="M26 20l20 13-20 13z" fill="rgba(255,255,255,.55)"/></svg>
  <div class="card-title">FretwiseRiffHall</div><div class="card-sub">Lorem ipsum dolor Sit Amet</div>
  <div class="share"><i></i><i></i><svg viewBox="0 0 20 16"><rect x="1" y="2" width="18" height="12" fill="#9a9a9a"/><path d="M1 2l9 7 9-7" fill="none" stroke="#333" stroke-width="1.3"/></svg><i></i><i></i></div>
</div>
<div class="video-card active" style="left:357px;top:900px">
  <div class="thumb" role="img" aria-label="Video still of a singer with guitar on stage, blue tint"></div><div class="shade"></div>
  <svg class="play" viewBox="0 0 66 66"><circle cx="33" cy="33" r="32" fill="#1c1c1c"/><path d="M26 20l20 13-20 13z" fill="#fff"/></svg>
  <div class="card-title">FretwiseRiffHall</div><div class="card-sub">Lorem ipsum dolor Sit Amet</div>
  <div class="share"><i></i><i></i><svg viewBox="0 0 20 16"><rect x="1" y="2" width="18" height="12" fill="#fff"/><path d="M1 2l9 7 9-7" fill="none" stroke="#1aa3d8" stroke-width="1.3"/></svg><i></i><i></i></div>
</div>
<div class="video-card" style="left:606px;top:900px">
  <div class="thumb" role="img" aria-label="Video still of a guitarist playing"></div><div class="shade"></div>
  <svg class="play" viewBox="0 0 66 66"><circle cx="33" cy="33" r="32" fill="rgba(255,255,255,.25)"/><path d="M26 20l20 13-20 13z" fill="rgba(255,255,255,.55)"/></svg>
  <div class="card-title">FretwiseRiffHall</div><div class="card-sub">Lorem ipsum dolor Sit Amet</div>
  <div class="share"><i></i><i></i><svg viewBox="0 0 20 16"><rect x="1" y="2" width="18" height="12" fill="#9a9a9a"/><path d="M1 2l9 7 9-7" fill="none" stroke="#333" stroke-width="1.3"/></svg><i></i><i></i></div>
</div>
<div class="video-card" style="left:855px;top:900px">
  <div class="thumb" role="img" aria-label="Video still of a guitarist playing"></div><div class="shade"></div>
  <svg class="play" viewBox="0 0 66 66"><circle cx="33" cy="33" r="32" fill="rgba(255,255,255,.25)"/><path d="M26 20l20 13-20 13z" fill="rgba(255,255,255,.55)"/></svg>
  <div class="card-title">FretwiseRiffHall</div><div class="card-sub">Lorem ipsum dolor Sit Amet</div>
  <div class="share"><i></i><i></i><svg viewBox="0 0 20 16"><rect x="1" y="2" width="18" height="12" fill="#9a9a9a"/><path d="M1 2l9 7 9-7" fill="none" stroke="#333" stroke-width="1.3"/></svg><i></i><i></i></div>
</div>

<div class="rule" style="top:1300px"></div>

<!-- Recently added -->
<div class="side-block" style="top:1370px">
  <h2>RECENTLY<br>ADDED LICKS</h2>
  <p>Lorem ipsum dolor sit amet, consectetur adipiscing elit, sed do eiusmod tempor incididunt ut labore et dolore magna aliqua.</p>
  <p>Ut enim ad minim veniam, quis nostrud exercitation ullamco laboris nisi ut aliquip ex ea commodo consequat..</p>
  <div class="pager">
    <span><svg width="10" height="10" viewBox="0 0 10 10"><path d="M6.5 1.5L3 5l3.5 3.5" fill="none" stroke="#fff" stroke-width="1.8"/></svg></span>
    <span><svg width="10" height="10" viewBox="0 0 10 10"><path d="M3.5 1.5L7 5 3.5 8.5" fill="none" stroke="#fff" stroke-width="1.8"/></svg></span>
  </div>
</div>
<div class="guitar" role="img" aria-label="Illustration of a red electric guitar" style="left:1084px;top:1282px;width:82px;height:422px;background:linear-gradient(#cfcfcf 0%,#a8a8a8 12%,#7a0c10 58%,#c0161e 75%,#4a0508 92%)"></div>

<div class="video-card" style="left:357px;top:1334px">
  <div class="thumb" role="img" aria-label="Video still of a singer with guitar"></div><div class="shade"></div>
  <svg class="play" viewBox="0 0 66 66"><circle cx="33" cy="33" r="32" fill="rgba(255,255,255,.25)"/><path d="M26 20l20 13-20 13z" fill="rgba(255,255,255,.55)"/></svg>
  <div class="card-title">FretwiseRiffHall</div><div class="card-sub">Lorem ipsum dolor Sit Amet</div>
  <div class="share"><i></i><i></i><svg viewBox="0 0 20 16"><rect x="1" y="2" width="18" height="12" fill="#9a9a9a"/><path d="M1 2l9 7 9-7" fill="none" stroke="#333" stroke-width="1.3"/></svg><i></i><i></i></div>
</div>
<div class="video-card" style="left:606px;top:1334px">
  <div class="thumb" role="img" aria-label="Video still of a guitarist playing"></div><div class="shade"></div>
  <svg class="play" viewBox="0 0 66 66"><circle cx="33" cy="33" r="32" fill="rgba(255,255,255,.25)"/><path d="M26 20l20 13-20 13z" fill="rgba(255,255,255,.55)"/></svg>
  <div class="card-title">FretwiseRiffHall</div><div class="card-sub">Lorem ipsum dolor Sit Amet</div>
  <div class="share"><i></i><i></i><svg viewBox="0 0 20 16"><rect x="1" y="2" width="18" height="12" fill="#9a9a9a"/><path d="M1 2l9 7 9-7" fill="none" stroke="#333" stroke-width="1.3"/></svg><i></i><i></i></div>
</div>
<div class="video-card" style="left:855px;top:1334px">
  <div class="thumb" role="img" aria-label="Video still of a guitarist on stage"></div><div class="shade"></div>
  <svg class="play" viewBox="0 0 66 66"><circle cx="33" cy="33" r="32" fill="rgba(255,255,255,.25)"/><path d="M26 20l20 13-20 13z" fill="rgba(255,255,255,.55)"/></svg>
  <div class="card-title">FretwiseRiffHall</div><div class="card-sub">Lorem ipsum dolor Sit Amet</div>
  <div class="share"><i></i><i></i><svg viewBox="0 0 20 16"><rect x="1" y="2" width="18" height="12" fill="#9a9a9a"/><path d="M1 2l9 7 9-7" fill="none" stroke="#333" stroke-width="1.3"/></svg><i></i><i></i></div>
</div>

<div class="rule" style="top:1735px"></div>

<!-- Most popular -->
<div class="side-block" style="top:1805px">
  <h2>MOST POPULAR<br>LICKS</h2>
  <p>Lorem ipsum dolor sit amet, consectetur adipiscing elit, sed do eiusmod tempor incididunt ut labore et dolore magna aliqua.</p>
  <p>Ut enim ad minim veniam, quis nostrud exercitation ullamco laboris nisi ut aliquip ex ea commodo consequat..</p>
  <div class="pager">
    <span><svg width="10" height="10" viewBox="0 0 10 10"><path d="M6.5 1.5L3 5l3.5 3.5" fill="none" stroke="#fff" stroke-width="1.8"/></svg></span>
    <span><svg width="10" height="10" viewBox="0 0 10 10"><path d="M3.5 1.5L7 5 3.5 8.5" fill="none" stroke="#fff" stroke-width="1.8"/></svg></span>
  </div>
</div>

<div class="video-card" style="left:357px;top:1768px">
  <div class="thumb" role="img" aria-label="Video still of a singer with guitar"></div><div class="shade"></div>
  <svg class="play" viewBox="0 0 66 66"><circle cx="33" cy="33" r="32" fill="rgba(255,255,255,.25)"/><path d="M26 20l20 13-20 13z" fill="rgba(255,255,255,.55)"/></svg>
  <div class="card-title">FretwiseRiffHall</div><div class="card-sub">Lorem ipsum dolor Sit Amet</div>
  <div class="share"><i></i><i></i><svg viewBox="0 0 20 16"><rect x="1" y="2" width="18" height="12" fill="#9a9a9a"/><path d="M1 2l9 7 9-7" fill="none" stroke="#333" stroke-width="1.3"/></svg><i></i><i></i></div>
</div>
<div class="video-card" style="left:606px;top:1768px">
  <div class="thumb" role="img" aria-label="Video still of a guitarist playing"></div><div class="shade"></div>
  <svg class="play" viewBox="0 0 66 66"><circle cx="33" cy="33" r="32" fill="rgba(255,255,255,.25)"/><path d="M26 20l20 13-20 13z" fill="rgba(255,255,255,.55)"/></svg>
  <div class="card-title">FretwiseRiffHall</div><div class="card-sub">Lorem ipsum dolor Sit Amet</div>
  <div class="share"><i></i><i></i><svg viewBox="0 0 20 16"><rect x="1" y="2" width="18" height="12" fill="#9a9a9a"/><path d="M1 2l9 7 9-7" fill="none" stroke="#333" stroke-width="1.3"/></svg><i></i><i></i></div>
</div>
<div class="video-card" style="left:855px;top:1768px">
  <div class="thumb" role="img" aria-label="Video still of a guitarist on stage"></div><div class="shade"></div>
  <svg class="play" viewBox="0 0 66 66"><circle cx="33" cy="33" r="32" fill="rgba(255,255,255,.25)"/><path d="M26 20l20 13-20 13z" fill="rgba(255,255,255,.55)"/></svg>
  <div class="card-title">FretwiseRiffHall</div><div class="card-sub">Lorem ipsum dolor Sit Amet</div>
  <div class="share"><i></i><i></i><svg viewBox="0 0 20 16"><rect x="1" y="2" width="18" height="12" fill="#9a9a9a"/><path d="M1 2l9 7 9-7" fill="none" stroke="#333" stroke-width="1.3"/></svg><i></i><i></i></div>
</div>

<!-- Blog -->
<h2 class="section-title" style="top:2193px">OUR BLOG</h2>
<div class="rule" style="top:2252px"></div>

<article class="post" style="left:110px;top:2294px">
  <div class="post-thumb" role="img" aria-label="Photo of hands on an electric guitar" style="background:linear-gradient(135deg,#1a1a1a,#6b6b6b 50%,#2a2a2a)"></div>
  <div class="post-body"><h3>Lorem Ipsum Dolor Sit Amet Consect-etur Adipisicing Elit</h3>
  <p>Lorem ipsum dolor sit amet, consectetur adipiscing elit, sed do eiusmod tempor incididunt ut labore et dolore magna aliqua.</p>
  <p>Ut enim ad minim veniam, quis nostrud exercitation ullamco laboris nisi ut aliquip ex ea commodo consequat..</p></div>
</article>
<article class="post" style="left:618px;top:2294px">
  <div class="post-thumb" role="img" aria-label="Photo of a guitarist on a purple-lit stage" style="background:linear-gradient(135deg,#2a1060,#7b4bd0 50%,#1a1040)"></div>
  <div class="post-body"><h3>Lorem Ipsum Dolor Sit Amet Consect-etur Adipisicing Elit</h3>
  <p>Lorem ipsum dolor sit amet, consectetur adipiscing elit, sed do eiusmod tempor incididunt ut labore et dolore magna aliqua.</p>
  <p>Ut enim ad minim veniam, quis nostrud exercitation ullamco laboris nisi ut aliquip ex ea commodo consequat..</p></div>
</article>
<article class="post" style="left:110px;top:2508px">
  <div class="post-thumb" role="img" aria-label="Photo of an acoustic guitar in warm light" style="background:linear-gradient(135deg,#3a1a05,#d88a2a 50%,#5a2a08)"></div>
  <div class="post-body"><h3>Lorem Ipsum Dolor Sit Amet Consect-etur Adipisicing Elit</h3>
  <p>Lorem ipsum dolor sit amet, consectetur adipiscing elit, sed do eiusmod tempor incididunt ut labore et dolore magna aliqua.</p>
  <p>Ut enim ad minim veniam, quis nostrud exercitation ullamco laboris nisi ut aliquip ex ea commodo consequat..</p></div>
</article>
<article class="post" style="left:618px;top:2508px">
  <div class="post-thumb" role="img" aria-label="Photo of a guitarist performing outdoors" style="background:linear-gradient(135deg,#1e2a22,#5e6e55 50%,#20281e)"></div>
  <div class="post-body"><h3>Lorem Ipsum Dolor Sit Amet Consect-etur Adipisicing Elit</h3>
  <p>Lorem ipsum dolor sit amet, consectetur adipiscing elit, sed do eiusmod tempor incididunt ut labore et dolore magna aliqua.</p>
  <p>Ut enim ad minim veniam, quis nostrud exercitation ullamco laboris nisi ut aliquip ex ea commodo consequat..</p></div>
</article>

<!-- Footer -->
<footer class="site-footer">
  <div class="footer-col" style="left:110px;width:220px">
    <h4><svg viewBox="0 0 14 14"><path d="M8 0L2 8h4l-1 6 6-8H7z" fill="#fff"/></svg>Quick Links</h4>
    <ul class="quick-links"><li>Home</li><li>About Us</li><li>Licks</li><li>jamtracks</li><li>Blog</li><li>Contact Us</li></ul>
    <div class="footer-social"><i></i><i></i><svg width="20" height="16" viewBox="0 0 20 16"><rect x="1" y="2" width="18" height="12" fill="#e0e0e0"/><path d="M1 2l9 7 9-7" fill="none" stroke="#111" stroke-width="1.3"/></svg><i></i><i></i></div>
  </div>
  <div class="footer-col comments" style="left:378px">
    <h4><svg viewBox="0 0 14 14"><circle cx="7" cy="4" r="3.2" fill="#fff"/><path d="M1 14c0-4 3-6 6-6s6 2 6 6z" fill="#fff"/></svg>Customer Comments</h4>
    <div class="comment"><div class="avatar"></div><div class="comment-text"><small>About 14 days ago</small><p>Lorem ipsum dolor sit amet consectetur adipisicing elit, Sed do euismod tempor incidunt ut labore et dolore magna aliqua.</p></div></div>
    <div class="comment"><div class="avatar"></div><div class="comment-text"><small>About 14 days ago</small><p>Lorem ipsum dolor sit amet consectetur adipisicing elit, Sed do euismod tempor incidunt ut labore et dolore magna aliqua.</p></div></div>
  </div>
  <div class="footer-col newsletter" style="left:776px">
    <h4><svg viewBox="0 0 14 14"><rect x=".8" y="2.5" width="12.4" height="9" fill="none" stroke="#fff" stroke-width="1.3"/><path d="M1 3l6 5 6-5" fill="none" stroke="#fff" stroke-width="1.3"/></svg>Newsletter</h4>
    <p>Lorem ipsum dolor sit amet consectetur adipisicing elit, Sed do euismod tempor incidunt ut labore et dolore magna aliqua...</p>
    <div class="email-field">E-mail</div>
    <div class="submit-btn">Submit Here</div>
  </div>
</footer>

<div class="bottom-bar">
  <span class="copy">Copyrights ©2015 FretwiseRiffHall.com - All Rights reserved</span>
  <span class="legal">Privacy Policy &nbsp; | &nbsp; Terms Of Uses</span>
</div>

</body>
</html>
```